Tidewell Consulting Schedule Of Rates

We need a brochure / proposal for our new company. Our company is a start up based in Australia who provides engineering and sales support to other renewable energy companies. Our brochure is a pitch-deck / sales item that catalogues our key services. We are engineering consultants.

Our website is www.tidewellpartners.com.au. Please review the website to get a feel of colour schemes etc.

We are looking for a strong, trustworthy feel, but the brochure also needs to be sales driven and to the point.

The second page that contains the $30 price point needs to be loud and clear.

The use of relevant icons throughout the document will be viewed favorably.

Please format the tables to look attractive.

The document will need to be in an editable format so content can be edited by us at a later date.

Please feel free to use the pics within the attached word document. The winning design will be provided with updated, clearer images upon request.

Thank you

Target Market(s)

Businesses that either sell or install solar PV and other renewable energy systems in Australia. Most of target market are likely to be electrical contractors.

Industry/Entity Type

Engineering

Colors
0255a3
0492cd
ffffff

Requirements
Must have
• Icons, graphics presentation, Clean and Clear, Business oriented. Sharp sales feel
Nice to have
• solar picture backgrounds maybe
Should not have
• cartoons, over sales driven,

```html
<!DOCTYPE html>
<html lang="en">
<head>
<meta charset="utf-8">
<title>Tidewell Consulting – Schedule of Rates</title>
<link href="https://fonts.googleapis.com/css2?family=Raleway:wght@300;400&family=Montserrat:wght@400;700&display=swap" rel="stylesheet">
<style>
:root{
  --navy:#0255a3;
  --sky:#0492cd;
  --ink:#2f2f2f;
  --white:#ffffff;
  --stage:#6f6f6f;
  --bezel:#1c1c1c;
  --silver:#c9cbcd;
}
*{box-sizing:border-box;margin:0;padding:0}
html,body{width:1200px;height:858px;overflow:hidden}
body{background:var(--stage);position:relative;font-family:"Montserrat",sans-serif;color:var(--ink)}
.spread{position:absolute;left:36px;width:1128px;display:flex}
.spread--top{top:28px;height:400px}
.spread--bottom{top:448px;height:380px}

/* ---------- Services page ---------- */
.page-services{width:564px;height:100%;background:linear-gradient(90deg,#e9e9e9,#f4f4f4 80%,#dcdcdc);position:relative;overflow:hidden}
.group-label{position:absolute;top:24px;font-family:"Raleway",sans-serif;font-weight:300;font-size:16px;color:var(--sky);white-space:nowrap;transform:translateX(-50%)}
.bracket{position:absolute;left:0;top:0}
.monitor{position:absolute;display:flex;flex-direction:column;align-items:center}
.monitor .bezel{background:var(--bezel);border-radius:4px 4px 0 0;padding:6px 6px 4px;width:100%}
.monitor .screen{background:var(--white);width:100%;overflow:hidden}
.monitor .chin{background:var(--silver);width:100%;height:12px;border-radius:0 0 3px 3px}
.monitor .neck{width:22%;height:14px;background:linear-gradient(#bbb,#e1e1e1)}
.monitor .foot{width:34%;height:3px;background:#d4d4d4;border-radius:2px}
.service{position:absolute;top:232px;width:150px;text-align:center}
.service h3{font-size:7.2px;font-weight:700;color:var(--navy);line-height:1.35;margin-bottom:11px}
.service p{font-size:6.9px;line-height:1.38;color:#444}

/* ---------- Design process page ---------- */
.page-process{width:564px;height:100%;position:relative;overflow:hidden}
.photo{position:absolute;inset:0}
.photo--process{background:radial-gradient(ellipse at 70% 30%,#2c6aa8 0%,#134078 45%,#071b3a 100%)}
.process-title{position:absolute;left:0;right:0;top:134px;text-align:center;font-family:"Raleway",sans-serif;font-weight:300;font-size:30px;color:var(--white);letter-spacing:.5px}
.step{position:absolute;top:179px;width:130px;display:flex;flex-direction:column;align-items:center;transform:translateX(-50%)}
.step-icon{width:70px;height:70px}
.step-label{font-family:"Raleway",sans-serif;font-weight:300;font-size:15px;color:var(--white);margin-top:4px;white-space:nowrap}
.step .monitor{position:relative;width:110px;margin-top:8px}

/* ---------- Bottom spread ---------- */
.photo-panel{width:350px;height:100%;position:relative}
.photo--engineer{background:linear-gradient(135deg,#1f5e9c 0%,#2a78b8 45%,#134a80 100%)}
.offer-column{width:214px;height:100%;background:var(--white);position:relative}
.offer{position:absolute;left:24px;width:168px}
.offer-icon{width:48px;height:48px;display:block;margin-bottom:3px}
.offer h4{font-size:7.2px;font-weight:700;color:var(--sky);margin-bottom:1px}
.offer p{font-size:6.6px;line-height:1.32;color:#555;text-align:justify}
.offer .cta{color:var(--sky);font-style:italic;margin-top:6px;text-align:left}
.page-about{width:564px;height:100%;position:relative;overflow:hidden}
.photo--crew{background:linear-gradient(160deg,#0d5ea6 0%,#1a7ac0 50%,#2b89c9 100%)}
.about{position:absolute;left:24px;top:26px;width:168px;color:var(--white)}
.about h2{font-family:"Raleway",sans-serif;font-weight:300;font-size:16px;margin-bottom:8px}
.about p{font-size:6.8px;line-height:1.32;text-align:justify;margin-bottom:10px}
.about ul{list-style:none;font-size:6.8px;line-height:1.32}
.about li::before{content:"• "}
</style>
</head>
<body>

<!-- ================= TOP SPREAD ================= -->
<section class="spread spread--top">
  <div class="page-services">
    <span class="group-label" style="left:194px">PVSim &nbsp;/ Interval Data</span>
    <span class="group-label" style="left:457px">Shading Modeling</span>
    <svg class="bracket" width="564" height="100" aria-hidden="true">
      <g stroke="#0492cd" stroke-width="0.8" fill="none">
        <path d="M107 72 V50 H282 V72 M194 50 V42"/>
        <path d="M457 42 V72"/>
      </g>
    </svg>

    <div class="monitor" style="left:27px;top:78px;width:160px">
      <div class="bezel"><div class="screen" style="height:100px">
        <svg width="148" height="100" viewBox="0 0 148 100" aria-hidden="true">
          <g fill="#999"><rect x="6" y="6" width="60" height="2"/><rect x="6" y="11" width="40" height="2"/><rect x="80" y="6" width="60" height="2"/><rect x="80" y="11" width="50" height="2"/></g>
          <rect x="6" y="26" width="64" height="34" fill="none" stroke="#aaa" stroke-width=".5"/>
          <g fill="#a31c22"><rect x="10" y="42" width="4" height="16"/><rect x="16" y="38" width="4" height="20"/><rect x="22" y="46" width="4" height="12"/><rect x="28" y="48" width="4" height="10"/><rect x="34" y="50" width="4" height="8"/><rect x="40" y="47" width="4" height="11"/><rect x="46" y="44" width="4" height="14"/><rect x="52" y="36" width="4" height="22"/><rect x="58" y="34" width="4" height="24"/></g>
          <rect x="76" y="26" width="66" height="34" fill="none" stroke="#aaa" stroke-width=".5"/>
          <g fill="#a31c22"><rect x="80" y="32" width="5" height="26"/><rect x="87" y="34" width="5" height="24"/><rect x="94" y="33" width="5" height="25"/><rect x="101" y="35" width="5" height="23"/><rect x="108" y="32" width="5" height="26"/><rect x="115" y="34" width="5" height="24"/><rect x="122" y="33" width="5" height="25"/><rect x="129" y="35" width="5" height="23"/></g>
          <g stroke="#bbb" stroke-width=".5"><path d="M20 70 H140 M20 76 H140 M20 82 H140 M20 88 H140 M20 94 H140"/><path d="M40 68 V96 M60 68 V96 M80 68 V96 M100 68 V96 M120 68 V96"/></g>
        </svg>
      </div></div>
      <div class="chin"></div><div class="neck"></div><div class="foot"></div>
    </div>

    <div class="monitor" style="left:202px;top:78px;width:160px">
      <div class="bezel"><div class="screen" style="height:100px">
        <svg width="148" height="100" viewBox="0 0 148 100" aria-hidden="true">
          <g fill="#bbb"><rect x="4" y="3" width="40" height="2"/><rect x="4" y="35" width="40" height="2"/><rect x="4" y="67" width="40" height="2"/></g>
          <g id="wave">
            <rect x="4" y="8" width="140" height="22" fill="#e8eef4"/>
            <path d="M4 30 C12 30 14 14 20 14 C26 14 28 30 36 30 C44 30 46 14 52 14 C58 14 60 30 68 30 C76 30 78 14 84 14 C90 14 92 30 100 30 C108 30 110 14 116 14 C122 14 124 30 132 30 L144 30Z" fill="#e2b21e"/>
            <path d="M4 30 C14 30 16 22 20 22 C24 22 26 30 36 30 C46 30 48 22 52 22 C56 22 58 30 68 30 C78 30 80 22 84 22 C88 22 90 30 100 30 C110 30 112 22 116 22 C120 22 122 30 132 30 L144 30Z" fill="#2f65a8"/>
          </g>
          <use href="#wave" y="32"/><use href="#wave" y="64"/>
        </svg>
      </div></div>
      <div class="chin"></div><div class="neck"></div><div class="foot"></div>
    </div>

    <div class="monitor" style="left:377px;top:78px;width:160px">
      <div class="bezel"><div class="screen" style="height:100px;background:linear-gradient(#ffffff,#eef0f4)" role="img" aria-label="3D shading model of a PV array and surrounding obstacles"></div></div>
      <div class="chin"></div><div class="neck"></div><div class="foot"></div>
    </div>

    <div class="service" style="left:32px">
      <h3>PvSim Report<br>$130 Ex Gst</h3>
      <p>PVSim is the industry leading PV performance simulation software globally. This program provides an highly accurate annual PV production report to assist financial forecasting, system optimization, performance warranties, etc. Our PV engineers can provide an accurate, tailored PVSim report for your solar project as required. If 3D shading loss is required in the report, please contact us for a tailored quotation.</p>
    </div>
    <div class="service" style="left:207px">
      <h3>Interval Data Analysis<br>$230 Ex Gst</h3>
      <p>Interval data analysis is becoming an increasingly important tool for commercial and utility scale solar design, helping to determine optimum PV system size, storage sizing, financial forecasts and grid integration. We are able to combine PVSim production data with your clients load interval data. This is usually provided in 60 minute intervals for a calendar year along with graphical representations.</p>
    </div>
    <div class="service" style="left:382px">
      <h3>Shading Report - $380 - $1500<br>Ex Gst (Case by Case)</h3>
      <p>Of course, nearby shading obstacles can ruin any performance estimate unless they are accounted for. We can integrate a 3D shading analysis with your PVSim report or drawing, helping to provide you with the most accurate performance modeling currently available. This service also assists in system design optimisation, e.g. selecting DC optimized vs standard PV modules.</p>
    </div>
  </div>

  <div class="page-process">
    <div class="photo photo--process" role="img" aria-label="Engineers reviewing system designs at computer screens, blue toned"></div>
    <h1 class="process-title">DESIGN PROCESS</h1>

    <div class="step" style="left:80px">
      <svg class="step-icon" viewBox="0 0 70 70" aria-hidden="true"><g fill="none" stroke="#fff" stroke-width="1.2"><circle cx="35" cy="35" r="34"/><circle cx="35" cy="35" r="30" stroke-width=".6"/><rect x="19" y="34" width="8" height="14"/><rect x="31" y="27" width="8" height="21"/><rect x="43" y="21" width="8" height="27"/></g></svg>
      <span class="step-label">Data Analysis</span>
      <div class="monitor"><div class="bezel"><div class="screen" style="height:60px">
        <svg width="98" height="60" viewBox="0 0 98 60" aria-hidden="true"><rect x="4" y="4" width="90" height="2" fill="#bbb"/><g fill="#a31c22"><rect x="8" y="24" width="6" height="22"/><rect x="17" y="28" width="6" height="18"/><rect x="26" y="34" width="6" height="12"/><rect x="35" y="36" width="6" height="10"/><rect x="44" y="32" width="6" height="14"/><rect x="53" y="26" width="6" height="20"/><rect x="62" y="20" width="6" height="26"/></g><path d="M6 46 H92 M6 52 H92" stroke="#bbb" stroke-width=".5"/></svg>
      </div></div><div class="chin" style="height:9px"></div><div class="neck" style="height:9px"></div><div class="foot"></div></div>
    </div>

    <div class="step" style="left:215px">
      <svg class="step-icon" viewBox="0 0 70 70" aria-hidden="true"><g fill="none" stroke="#fff" stroke-width="1.2"><circle cx="35" cy="35" r="34"/><circle cx="35" cy="35" r="30" stroke-width=".6"/><path d="M20 26 L26 20 L52 46 L46 52Z"/><path d="M50 18 L54 22 L28 48 L20 52 L22 44Z"/></g></svg>
      <span class="step-label">Design Stage</span>
      <div class="monitor"><div class="bezel"><div class="screen" style="height:60px;background:#cfcfcf">
        <svg width="98" height="60" viewBox="0 0 98 60" aria-hidden="true"><rect x="10" y="6" width="78" height="48" fill="#fff" stroke="#888" stroke-width=".5"/><g stroke="#c23" stroke-width="2"><path d="M14 12 H84 M14 20 H84 M14 28 H84 M14 36 H84 M14 44 H84"/></g><g stroke="#37b" stroke-width="1"><path d="M30 10 V50 M50 10 V50 M70 10 V50"/></g></svg>
      </div></div><div class="chin" style="height:9px"></div><div class="neck" style="height:9px"></div><div class="foot"></div></div>
    </div>

    <div class="step" style="left:350px">
      <svg class="step-icon" viewBox="0 0 70 70" aria-hidden="true"><g fill="none" stroke="#fff" stroke-width="1.2"><circle cx="35" cy="35" r="34"/><circle cx="35" cy="35" r="30" stroke-width=".6"/><circle cx="42" cy="26" r="7" stroke-dasharray="3 2" stroke-width="3"/><circle cx="42" cy="26" r="3"/><circle cx="27" cy="38" r="8" stroke-dasharray="3 2" stroke-width="3"/><circle cx="27" cy="38" r="3"/><circle cx="44" cy="47" r="7" stroke-dasharray="3 2" stroke-width="3"/><circle cx="44" cy="47" r="3"/></g></svg>
      <span class="step-label">Concept Stage</span>
      <div class="monitor"><div class="bezel"><div class="screen" style="height:60px;background:#b9a47c" role="img" aria-label="Aerial view of a rooftop with panel layout"></div></div><div class="chin" style="height:9px"></div><div class="neck" style="height:9px"></div><div class="foot"></div></div>
    </div>

    <div class="step" style="left:486px">
      <svg class="step-icon" viewBox="0 0 70 70" aria-hidden="true"><g fill="none" stroke="#fff" stroke-width="1.2"><circle cx="35" cy="35" r="34"/><circle cx="35" cy="35" r="30" stroke-width=".6"/><path d="M22 48 L46 24 M46 24 C44 18 50 14 54 16 L49 21 L51 23 L56 18 C58 22 54 28 48 26"/><path d="M48 48 L26 26 M20 22 L24 18 L30 24 L26 28Z"/></g></svg>
      <span class="step-label">Final Stage</span>
      <div class="monitor"><div class="bezel"><div class="screen" style="height:60px;background:linear-gradient(#c9d2dc,#8a9cb0 60%,#6d7a86)" role="img" aria-label="Completed commercial rooftop solar installation"></div></div><div class="chin" style="height:9px"></div><div class="neck" style="height:9px"></div><div class="foot"></div></div>
    </div>
  </div>
</section>

<!-- ================= BOTTOM SPREAD ================= -->
<section class="spread spread--bottom">
  <div class="photo-panel">
    <div class="photo photo--engineer" role="img" aria-label="Smiling engineer in a hard hat working on solar panels, blue toned"></div>
  </div>

  <div class="offer-column">
    <div class="offer" style="top:22px">
      <svg class="offer-icon" viewBox="0 0 48 48" aria-hidden="true"><circle cx="24" cy="24" r="24" fill="#0492cd"/><g fill="none" stroke="#fff" stroke-width="1"><path d="M19 38 L24 10 L29 38 M20 32 H28 M21 24 H27 M22 17 H26 M20 32 L27 24 M28 32 L21 24 M21 24 L26 17 M27 24 L22 17 M16 15 H32"/></g></svg>
      <h4>Grid Services Above 150kW</h4>
      <p>Our in house team has experience in design and delivery of multiple large scale PV projects including rooftop, ground mounted, LV, HV systems. Systems above 150kW often require more complex integration such as PFC, load shedding, communications integration etc. We are experienced and equipped to meet these needs.</p>
    </div>
    <div class="offer" style="top:160px">
      <svg class="offer-icon" viewBox="0 0 48 48" aria-hidden="true"><circle cx="24" cy="24" r="24" fill="#0492cd"/><g fill="none" stroke="#fff" stroke-width="1.2"><path d="M18 12 V20 M30 12 V20 M14 20 H34 V26 C34 32 30 34 24 34 C18 34 14 32 14 26Z M24 34 V40"/></g></svg>
      <h4>Protection Relay Board</h4>
      <p>If your system requires a custom design Grid Protection Relay Board, we can help.</p>
    </div>
    <div class="offer" style="top:250px">
      <svg class="offer-icon" viewBox="0 0 48 48" aria-hidden="true"><circle cx="24" cy="24" r="24" fill="#0492cd"/><g fill="none" stroke="#fff" stroke-width="1.2"><rect x="12" y="18" width="24" height="16"/><path d="M16 18 V15 H20 V18 M28 18 V15 H32 V18"/></g></svg>
      <h4>Off Grid / Batteries</h4>
      <p style="text-align:left">As well as working with industry leading brands and partners, our accredited engineers can assist you in your project specific storage design requirements.</p>
      <p class="cta">Please contact us to discuss<br>your project requirements.</p>
    </div>
  </div>

  <div class="page-about">
    <div class="photo photo--crew" role="img" aria-label="Installation crew in hard hats fitting solar panels on a roof, blue toned"></div>
    <div class="about">
      <h2>About Us</h2>
      <p>Our team of renewable energy experts specialise in project development, feasibility studies, system design and delivery. We have successfully delivered over 40MW of commercial and utility renewable energy systems; our team has proven capability in this space.</p>
      <p>With our in-house team of engineers, designers, and business analysts, the Tidewell Consulting team has the expertise and dedication to provide your business with a superior design solution.</p>
      <p>We utilize our real-life experience, industry leading software and trusted industry partners to provide an optimum and cost effective energy solution for our customers. Some of the key services we offer in this area are:</p>
      <ul>
        <li>Grid tied and off-grid renewable energy design.</li>
        <li>Battery Storage design and integration.</li>
        <li>Energy data analysis and modelling</li>
        <li>DNSP and other relevant approvals</li>
        <li>Electrical Installation Design</li>
      </ul>
    </div>
  </div>
</section>

</body>
</html>
```